Architectural Footbridge Poster / Board

We are a design company specializing in bridge design and engineering. We have developed a footbridge design intended for use in local parks within New Zealand. With the help of our friends here at Sketch Huddle have created 3D render of our bridge that we need turned into striking posters that can be used to advertise the bridge to local councils, architects, and private developers.

We have attached a series of high resolution raw images that we would like used in our posters. Feel free to select and/or crop the images to fit with your poster style. We have also included all of the text that we need added (see below). We would like the posters to appear professional but artistic/fun. We have created a quick mock-up using MS Word to give you an idea of what we need. Please note we expect the designers to vastly improve or in many cases drastically change these quick mock-ups and we will be looking at composition, alignment/layout, and style. Once we have an entry that we feel provide a high quality visual poster we will guarantee the payment.
The competition will be based on producing 2 posters: page 1 and page 2 as per the attached poster content.

• Poster layout must be landscape.
• Raw "InDesign", or "MS Word" or other pre-approved raw file must be supplied to receive payment. Alternative file types can be pre-approved via the comments field.
• The posters must be high resolution PDF to size A0.
• The poster will also be printed at A3. Minimum font size when viewed in A3 should be size 8 and readable (size 9 is preferred). Images can go all the way to the outside of the page but A3 text margins must be set a minimum 0.4cm from top and bottom and 1cm left and right.
• Some examples of architecture board styles that we like have been put in a Pinterest folder here: https://uk.pinboardly.example/MarkVellisonPEng/architecture-display-board/
• If you think your style would be better achieved by splitting each page into two this will be considered if it lends significant style advantages. We will try to provide early feedback on this if we see good examples.
• Along the way we will be providing detailed feedback to our designers as required.
• If you need more text or info for a particular poster style let us know. Requesting more text is fine but further 3d renders are not possible. We will try to provide additional text as requested.
• We have included a company logo that was created very quickly by our team. Feel free to modify or improve this logo if it improves your poster design. Merit will be given to posters that significantly improve our logo. Our company creates vibrant and interesting footbridges.

Please be as creative as you can. If we like your style there is the potential for future work doing similar poster work for alternative bridge designs.

Let us know if you have any questions.

Target Market(s)

landscape architects, local councils

Industry/Entity Type

It Company

Requirements
Must have
• 1) Landscape orientation
• 2) Printable (and readable) at both A0 and A3
• 3) Raw InDesign, Photoshop, MS Word or other pre-approved raw file type.
Nice to have
• Posters should be image focussed with text being less prominent.

```html
<!DOCTYPE html>
<html lang="en">
<head>
<meta charset="utf-8">
<title>NZ Pedestrian Footbridge – Kereru Span Studio</title>
<link href="https://fonts.googleapis.com/css2?family=Montserrat:wght@400;500;700;900&display=swap" rel="stylesheet">
<style>
  :root {
    --yellow: #ffd21f;
    --ink: #0d0d0d;
    --panel: #101010;
    --panel-side: #262626;
    --paper: #ffffff;
    --photo-dark: #2b2b2b;
    --photo-mid: #6d6d6d;
    --photo-light: #c9c9c9;
    --label: #1a1a1a;
  }
  * { box-sizing: border-box; margin: 0; padding: 0; }
  html, body { width: 1200px; height: 848px; overflow: hidden; background: var(--paper); }
  .board {
    position: relative; width: 1200px; height: 848px; overflow: hidden;
    background: var(--paper);
    font-family: "Montserrat", Arial, sans-serif;
  }
  .park-scene {
    position: absolute; inset: 0;
    background:
      radial-gradient(ellipse at 70% 20%, var(--photo-light) 0%, transparent 45%),
      radial-gradient(ellipse at 55% 75%, #9a9a9a 0%, transparent 50%),
      linear-gradient(180deg, var(--photo-dark) 0%, var(--photo-mid) 55%, #8a8a8a 100%);
    clip-path: polygon(0 0, 100% 0, 100% 520px, 0 650px);
  }
  .accent-band {
    position: absolute; inset: 0;
    background: var(--yellow);
    clip-path: polygon(420px 598px, 1200px 520px, 1200px 848px, 668px 848px);
  }
  .info-panel {
    position: absolute; left: 24px; top: 34px; width: 396px; height: 730px;
  }
  .info-panel__side {
    position: absolute; left: 0; top: 0; width: 100%; height: 100%;
  }
  .info-panel__body {
    position: absolute; left: 22px; top: 60px; width: 352px;
    color: #f2f2f2; font-size: 7.6px; line-height: 1.38; font-weight: 400;
  }
  .info-panel__body p { margin-bottom: 8.5px; }
  .info-panel__body strong { font-weight: 700; color: #fff; }
  .headline {
    position: absolute; left: 436px; top: 46px;
    color: var(--yellow); font-weight: 900; font-size: 84px; line-height: 76px;
    letter-spacing: -0.5px; text-transform: uppercase; white-space: nowrap;
  }
  .subhead {
    position: absolute; left: 440px; top: 230px;
    color: var(--paper); font-weight: 700; font-size: 21.5px; letter-spacing: 0.2px;
    text-transform: uppercase; white-space: nowrap;
  }
  .detail-disc {
    position: absolute; left: 626px; top: 312px; width: 552px; height: 552px;
    border-radius: 50%; background: var(--paper);
  }
  .bridge-render {
    position: absolute; left: 770px; top: 482px; width: 268px; height: 190px;
    border-radius: 14px;
    background: linear-gradient(160deg, #8fc3d6 0%, #a2582f 45%, #7a3d1f 75%, #9aa8b0 100%);
  }
  .callouts { position: absolute; inset: 0; pointer-events: none; }
  .callout {
    position: absolute; color: var(--label); font-size: 8.4px; font-weight: 500;
    line-height: 1.25; text-transform: uppercase;
  }
  .callout--center { text-align: center; }
  .studio-name {
    position: absolute; left: 34px; top: 776px;
    color: var(--ink); font-weight: 900; font-size: 29px; letter-spacing: -1.2px;
    text-transform: uppercase; white-space: nowrap;
  }
</style>
</head>
<body>
<main class="board">
  <div class="park-scene" role="img" aria-label="Black and white photo of a family walking across the timber footbridge with wire balustrade through a wooded park"></div>
  <div class="accent-band"></div>

  <section class="info-panel">
    <svg class="info-panel__side" viewBox="0 0 396 730" preserveAspectRatio="none" aria-hidden="true">
      <polygon points="0,0 396,14 396,730 0,716" fill="var(--panel)"/>
      <polygon points="380,13 396,14 396,730 380,722" fill="var(--panel-side)"/>
    </svg>
    <div class="info-panel__body">
      <p>This balustrade option features horizontal balustrade wires. Horizontal wires are a cost effective and low maintenance option for NZ bridges. The horizontal wire infill system is common place on New Zealand cycle bridges as they allow a lightweight aesthetic whilst proving a safe restraint to users*.</p>
      <p>Because the infill wires are made from stainless steel they provide optimal long-term durability compared to contemporary painted steel rod or steel plate infill systems. Using this system reduces overall fabrication and whole of life maintenance costs for the bridge</p>
      <p><strong>Fully code compliant.</strong> Designed for New Zealand applications in accordance with New Zealand Design Standards.</p>
      <p><strong>Spans up to 18m.</strong> Reduce by multiples of 1.8m for smaller spans e.g. can also work for 16.2m, 14.4m, etc.</p>
      <p><strong>Designed for 3.0m wide footways.</strong> Can be easily reduced to other widths without further design.</p>
      <p><strong>Balustrade heights of 1.1m.</strong> Posts are fabricated by cutting universal beams to reduce welding and fabrication costs.</p>
      <p><strong>Architectural flexibility.</strong> Alternative balustrade designs can be incorporated to enable the implementation of customised – but cost effective – project specific architectural merit.</p>
      <p><strong>Full colour versatility.</strong> The steelwork can be finished to a vast array of different colours including most of the Tuatara Paints and/or Harbourline Coatings colour palettes.</p>
      <p><strong>Includes full superstructure design drawings.</strong> Enables fast and simple detailed design and fabrication stages.</p>
      <p><strong>3D models available.</strong> SKP files can be provided so that the design can be quickly added to landscape architect or urban developer masterplans.</p>
      <p><strong>Good whole of life cost.</strong> The 100 year overall design life exceeds the NZ Building Code (NZBC) requirement of 50 years. Achieved with minimal additional cost thus providing good whole of life cost for clients. Time to first maintenance for steelwork paint systems is 40 years and timber replacement after 50 years.</p>
      <p><strong>Environmentally friendly.</strong> Acrylic elastomeric paint systems can be used directly over the existing paint system during bridge maintenance and touch-ups which prevents the need for sand blasting over waterways.</p>
      <p><strong>Thoughtful economic Vs. aesthetic balance.</strong> Only the visible elements of the steelwork are painted. All of the internal steelwork is galvanized or zinc sprayed. This provides an excellent balance of aesthetics to cost.</p>
      <p><strong>Safe and quick construction.</strong> Time on site can be significantly reduced by fabricating the entire superstructure (including balustrades) off-site. Bridge is designed to be transportable in single piece (depending upon site access). It can be lifted into place once the abutments are complete.</p>
      <p><strong>Cost effective solution.</strong> The estimate for this bridge is approximately $3,500 per metre square (+/-30% depending on site conditions, location, and project setup) = $190,000 for the 18m long x 3m wide version. Since this estimate includes all structural design, geotechnical and fabrication/erection costs (a full "no surprises" estimate for pricing purposes) it therefore represents a very cost effective solution for most applications. Consenting fees, construction monitoring, and adjoining paths for the bridge are assumed provided elsewhere in your masterplan costs.</p>
    </div>
  </section>

  <h1 class="headline">NZ Pedestrian<br>Footbridge</h1>
  <p class="subhead">With horizontal wire balustrade</p>

  <div class="detail-disc"></div>
  <div class="bridge-render" role="img" aria-label="3D cutaway of the footbridge showing timber decking, blue painted steel girders and posts, stainless wire balustrade and two people walking a dog"></div>

  <svg class="callouts" viewBox="0 0 1200 848" aria-hidden="true">
    <g stroke="var(--label)" stroke-width="1.6" stroke-dasharray="4 3" fill="none">
      <polyline points="820,504 820,468 1034,468 1034,510"/>
      <line x1="896" y1="526" x2="880" y2="526"/>
      <line x1="752" y1="526" x2="786" y2="526"/>
      <line x1="1040" y1="524" x2="1024" y2="524"/>
      <line x1="1070" y1="622" x2="1040" y2="622"/>
      <line x1="1040" y1="658" x2="1010" y2="658"/>
      <line x1="852" y1="682" x2="852" y2="664"/>
      <line x1="766" y1="696" x2="790" y2="668"/>
    </g>
  </svg>

  <p class="callout callout--center" style="left:868px; top:442px; width:76px;">3.0m<br>Usable width</p>
  <p class="callout" style="left:898px; top:518px; width:90px;">Hardwood timber decking</p>
  <p class="callout" style="left:680px; top:506px; width:70px;">1.1 m high balustrade posts @ 1.8 m centres</p>
  <p class="callout" style="left:1044px; top:512px; width:108px;">Stainless steel wires at 80 mm centres</p>
  <p class="callout" style="left:1074px; top:614px; width:64px;">Visible steel painted</p>
  <p class="callout" style="left:1044px; top:653px; width:100px;">Steel 'I' girder</p>
  <p class="callout callout--center" style="left:822px; top:684px; width:60px;">H 3.2 timber joints</p>
  <p class="callout callout--center" style="left:732px; top:698px; width:50px;">Steel cross beam</p>

  <p class="studio-name">Kereru Span Studio</p>
</main>
</body>
</html>
```